Create Vertical Dog Food Labels (3 inches x 5 inches) for PupKitchen

We need a packing Vertical label (3 inches x 5 inches) design for our line of Dog Food - Pup Kitchen at pupkitchenmeals.com (please review website). This design is for Custom Roll Labels. We have a logo already. Use our logo colors on label. What we need incorporated is a list of our ingredients:

50% Choice Beef
20% Pasture-raised Chicken
15% Brown Rice
15% Fresh Vegetables - Carrots, Kale, Zucchini
Herbal Health Boosters

We also need these lines at the bottom of the label:

Keeps in fridge for 4 days after thawing
Stores in freezer up to 6 months
Questions? email us at orders@meadowlanepantry.com

We have attached a sample of a competitor. The Kibble Crate.

Target Market(s)

Dog owners

Industry/Entity Type

Dog Food

Font styles to use
Sans Serif

Requirements
Must have
• Read project description above
Nice to have
• Our logo color incorporated
Should not have
• I want it simple.

```html
<!DOCTYPE html>
<html lang="en">
<head>
<meta charset="utf-8">
<title>PupKitchen – Nourishing Recipe For Dogs Label</title>
<link rel="stylesheet" href="https://fonts.googleapis.com/css2?family=Open+Sans:wght@400;700;800&family=Roboto+Condensed:wght@700&family=Libre+Caslon+Text:wght@700&display=swap">
<style>
  :root {
    --backdrop: #626262;
    --card: #ffffff;
    --header-cream: #fdf3cf;
    --brand-green: #1f6b32;
    --leaf-green: #6aaa3a;
    --ink: #111111;
    --ribbon-red: #ed1c24;
    --ribbon-dark: #a50f16;
    --panel-fill: #f4f4f4;
    --silhouette: #e2d6c7;
    --sky: #8fd0ef;
    --fur: #d8954a;
    --tan: #c2a36b;
    --badge-brown: #b79d84;
  }
  * { box-sizing: border-box; margin: 0; padding: 0; }
  html, body { width: 778px; height: 1200px; overflow: hidden; }
  body {
    background: var(--backdrop);
    font-family: "Open Sans", Arial, sans-serif;
    color: var(--ink);
    position: relative;
  }
  .label {
    position: absolute; left: 71px; top: 69px;
    width: 637px; height: 1061px;
    background: var(--card);
    border-radius: 22px;
    overflow: hidden;
  }
  .label > * { position: absolute; }

  .brand-band {
    left: 0; top: 30px; width: 100%; height: 173px;
    background: var(--header-cream);
  }
  .brand-dot {
    left: 106px; top: 58px; width: 110px; height: 110px;
    border-radius: 50%; background: var(--leaf-green);
  }
  .brand-name {
    left: 236px; top: 82px;
    font-size: 46px; font-weight: 400; color: var(--brand-green);
    letter-spacing: 1px;
  }

  .recipe-title {
    left: 0; width: 100%; top: 222px; text-align: center;
    font-size: 68px; font-weight: 800; letter-spacing: -2px;
  }

  .ribbon { left: 212px; top: 308px; width: 400px; height: 116px; }
  .ribbon-text {
    left: 259px; top: 312px; width: 330px; text-align: center;
    font-size: 58px; font-weight: 700; color: #fff; letter-spacing: -1px;
  }
  .dog-photo {
    left: 81px; top: 305px; width: 140px; height: 140px;
    border-radius: 50%; border: 5px solid #fff;
    background: radial-gradient(circle at 50% 65%, var(--fur) 0 45%, var(--sky) 46%);
  }

  .silhouette { background: var(--silhouette); }
  .silhouette.steak { left: 323px; top: 415px; width: 77px; height: 47px; border-radius: 40% 50% 45% 40%; }
  .silhouette.cow { left: 0; top: 462px; width: 105px; height: 99px; border-radius: 30% 45% 20% 20%; }
  .silhouette.carrot { left: 550px; top: 458px; width: 77px; height: 77px; border-radius: 50% 10% 50% 50%; }
  .silhouette.chicken { left: 0; top: 655px; width: 79px; height: 103px; border-radius: 20% 50% 50% 30%; }
  .silhouette.kale { left: 554px; top: 638px; width: 83px; height: 99px; border-radius: 50% 0 0 50%; }

  .ingredients {
    left: 119px; top: 488px; width: 414px; height: 273px;
    border: 2px solid var(--ink); border-radius: 30px;
    background: var(--panel-fill);
  }
  .ingredient { position: absolute; text-align: center; }
  .ingredient .rule { height: 2px; background: var(--ink); margin: 0 auto; }
  .ingredient .percent {
    font-family: "Libre Caslon Text", Georgia, serif;
    font-size: 52px; font-weight: 700; line-height: 1; margin-top: 8px;
  }
  .ingredient .percent small { font-size: 32px; }
  .ingredient .name {
    display: block; margin: 6px auto 0;
    background: var(--ribbon-red); color: #fff; border-radius: 9px;
    font-family: "Roboto Condensed", Arial, sans-serif; font-weight: 700;
    font-size: 22px; line-height: 1.05; padding: 4px 6px;
  }
  .ingredient .name small { font-size: 15px; }
  .beef { left: 26px; top: 14px; width: 147px; }
  .rice { left: 230px; top: 14px; width: 146px; }
  .chicken-cell { left: 21px; top: 139px; width: 165px; }
  .veg { left: 209px; top: 139px; width: 188px; }
  .beef .rule, .rice .rule { width: 144px; }
  .chicken-cell .rule { width: 173px; margin-left: -8px; }
  .veg .rule { width: 186px; }
  .chicken-cell .name, .veg .name { padding: 6px 4px; }

  .storage {
    left: 0; top: 810px; width: 441px; height: 76px;
    border-top: 2px solid var(--ink); border-bottom: 2px solid var(--ink);
    padding: 8px 0 0 19px;
    font-family: "Roboto Condensed", Arial, sans-serif; font-weight: 700;
    font-size: 22px; line-height: 30px; list-style: none;
  }
  .storage li::before { content: "– "; }

  .herbal-badge {
    left: 458px; top: 769px; width: 150px; height: 150px; border-radius: 50%;
    border: 6px solid var(--badge-brown);
    display: flex; align-items: center; justify-content: center; text-align: center;
    font-size: 18px; line-height: 18px; color: #222; padding-top: 16px;
  }

  .contact {
    left: 0; top: 932px; width: 100%; height: 98px;
    background: var(--tan); color: #fff; text-align: center;
  }
  .contact-heading {
    font-family: "Roboto Condensed", Arial, sans-serif; font-weight: 700;
    font-size: 24px; letter-spacing: 1.5px; padding-top: 9px;
  }
  .contact-rule { width: 512px; height: 1px; background: #fff; margin: 9px auto 0; }
  .contact-email { font-size: 32px; font-weight: 400; letter-spacing: 1px; line-height: 42px; }
</style>
</head>
<body>
  <main class="label">
    <div class="brand-band"></div>
    <div class="brand-dot"></div>
    <div class="brand-name">PupKitchen</div>

    <h1 class="recipe-title">Nourishing Recipe</h1>

    <svg class="ribbon" viewBox="0 0 400 116" aria-hidden="true">
      <polygon points="330,72 400,72 380,96 398,116 318,116" fill="var(--ribbon-dark)"/>
      <path d="M20 20 Q190 -6 360 16 L372 96 Q190 74 26 100 Z" fill="var(--ribbon-red)"/>
    </svg>
    <div class="ribbon-text">For Dogs</div>
    <div class="dog-photo" role="img" aria-label="Photo of a happy corgi against a blue sky"></div>

    <div class="silhouette steak" role="img" aria-label="Faint steak silhouette"></div>
    <div class="silhouette cow" role="img" aria-label="Faint cow silhouette"></div>
    <div class="silhouette carrot" role="img" aria-label="Faint carrot silhouette"></div>
    <div class="silhouette chicken" role="img" aria-label="Faint chicken silhouette"></div>
    <div class="silhouette kale" role="img" aria-label="Faint kale leaf silhouette"></div>

    <section class="ingredients" aria-label="Ingredients">
      <div class="ingredient beef">
        <div class="rule"></div>
        <div class="percent">50<small>%</small></div>
        <span class="name">Choice Beef</span>
      </div>
      <div class="ingredient rice">
        <div class="rule"></div>
        <div class="percent">15<small>%</small></div>
        <span class="name">Brown Rice</span>
      </div>
      <div class="ingredient chicken-cell">
        <div class="rule"></div>
        <div class="percent">20<small>%</small></div>
        <span class="name">Pasture-raised<br>Chicken</span>
      </div>
      <div class="ingredient veg">
        <div class="rule"></div>
        <div class="percent">15<small>%</small></div>
        <span class="name">Fresh Vegetables<br><small>(Carrots, Kale, Zucchini)</small></span>
      </div>
    </section>

    <ul class="storage">
      <li>Keeps in fridge for 4 days after thawing</li>
      <li>Stores in freezer up to 6 months</li>
    </ul>

    <div class="herbal-badge">HERBAL<br>HEALTH<br>BOOSTERS</div>

    <footer class="contact">
      <div class="contact-heading">QUESTIONS? EMAIL US AT</div>
      <div class="contact-rule"></div>
      <div class="contact-email">orders@meadowlanepantry.com</div>
    </footer>
  </main>
</body>
</html>
```